Hi Designers,

I will need 4 web pages designed. The web page looks like an App (if you click on the logo, or the icon on an iPad, it will take you to the website), but it is still a webpage.

Please check the attachment on this brief to understand what specific pages I need to be designed.

A .PSD (straight-up PhotoShop image) as final deliverable is fine, as long as you give us the exact “web color numbers”.

The design is for desktop and iPad but in a single unified web application, NOT separate web app and (native) iPad app.

Details:

Bright Harbor Policy Systems is developing a browser-based application for use on any mobile device or desktop. The app will be used by corporations to communicate with their employees regarding legal, regulatory and company requirements for conducting business. The app is known as “Workplace Guidance Hub.” When the user clicks on the icon for Workplace Guidance Hub, they will enter a site full of information that a company deems necessary for the employee to do his/her job. There are several content sections within the site, including a login page, training, policies, forms, news feeds and blogs.

The application has been built using Microsoft .NET, and fully supports CSS-type skinning; it uses traditional page layouts. We are seeking a product logo concept (image), a master application/desktop icon (image), as well as a full color scheme/theme/skin design for all areas of the application (header area, body text, menu bar, etc.) in the form of a CSS. The look should be clean, crisp and professional; nothing cartoony or whimsical. It should be easy to read and “airy”.

We have sketched prototypes for the basic application page layout that we can send as a next step of the process.
Updates

Screen shots have been uploaded to this project.  Please use them to guide your design.

Dear designers,

I apologize for the delay in providing feedback. My partners and I will provide feedback in a few days. Thank you for your patience.

Industry/Entity Type

Business

Font styles to use
Other font styles liked:
• see font on screen shots when uploaded

```html
<!DOCTYPE html>
<html lang="en">
<head>
<meta charset="utf-8">
<title>Compliance Game</title>
<link href="https://fonts.googleapis.com/css2?family=Open+Sans:ital,wght@0,300;0,400;0,600;0,700;1,400&display=swap" rel="stylesheet">
<style>
:root{
  --bar-top:#3a3d41;
  --bar-bottom:#1f2124;
  --bar-active:#2a2c2f;
  --badge:#e8492b;
  --page:#f1efe9;
  --side:#f6fafd;
  --side-line:#d9dee2;
  --ink:#333;
  --ink-soft:#666;
  --ink-mute:#888;
  --card:#fff;
  --card-edge:#dedbd4;
  --row-alt:#ececec;
  --pill:#3a3a3a;
  --accent:#6e4a6e;
  --soc-a:#3b5a9a;
  --soc-b:#2aa9e0;
  --soc-c:#d9473a;
  --soc-d:#1a7ab8;
}
*{box-sizing:border-box;margin:0;padding:0}
html,body{width:1200px;height:834px;overflow:hidden}
body{font-family:"Open Sans",sans-serif;background:var(--page);color:var(--ink);position:relative}

/* top bar */
.topbar{position:absolute;left:0;top:0;width:1200px;height:49px;background:linear-gradient(var(--bar-top),var(--bar-bottom));color:#fff;font-size:13px;font-weight:600}
.nav-item{position:absolute;top:0;height:49px;display:flex;align-items:center;gap:9px}
.nav-item svg{width:16px;height:16px}
.nav-home{left:27px;width:112px;padding-left:12px;background:var(--bar-active)}
.badge{width:18px;height:18px;border-radius:50%;background:var(--badge);font-size:10px;display:flex;align-items:center;justify-content:center}
.nav-sep{position:absolute;top:13px;width:1px;height:24px;background:#55585c}
.top-search{position:absolute;left:506px;top:12px;width:197px;height:28px;border-radius:8px;background:#17191b;box-shadow:inset 0 1px 2px #000;display:flex;align-items:center;padding-left:12px;gap:16px;font-weight:400;color:#ddd}
.user{position:absolute;left:1066px;top:8px;display:flex;align-items:center;gap:10px;line-height:15px}
.avatar{width:32px;height:32px;border-radius:50%;background:radial-gradient(#c9a48a,#6d5a4e);border:2px solid #ddd}

/* sidebar */
.sidebar{position:absolute;left:0;top:49px;width:237px;height:755px;background:var(--side);border-right:1px solid var(--side-line)}
.side-title{position:absolute;left:14px;top:18px;font-size:12px;font-weight:700}
.side-search{position:absolute;left:10px;top:46px;width:195px;height:28px;border:2px solid #e3e6e8;border-radius:8px;background:#fff;display:flex;align-items:center;gap:10px;padding-left:9px;font-size:12px;color:#aaa}
.side-menu{position:absolute;left:0;top:98px;width:237px;list-style:none}
.side-menu li{height:50px;border-bottom:1px solid var(--side-line);display:flex;align-items:center;gap:16px;padding-left:12px;font-size:13px;font-weight:600;color:var(--ink-soft)}
.side-menu svg{width:28px;height:28px;fill:#b9bcbf}
.signin{position:absolute;left:16px;top:545px;width:212px}
.signin h2{font-size:23px;font-weight:400}
.signin p{font-size:14px;margin-top:12px}
.register{margin-top:14px;height:37px;border:1px solid #dcdfe1;background:#fff;font-size:13px;color:#666;padding:9px 4px}
.social{display:flex;gap:14px;margin-top:11px;margin-left:-2px}
.social span{width:32px;height:32px;border-radius:50%}
.copy{font-size:11px;font-weight:600;color:var(--ink-soft);margin-top:16px;margin-left:0}

/* main feed */
.section-title{position:absolute;font-size:14px;font-weight:600;display:flex;align-items:center;gap:6px}
.dots{width:11px;height:7px;background:radial-gradient(circle,var(--accent) 1.3px,transparent 1.6px) 0 0/4px 3.5px}
.category{position:absolute;left:281px;top:121px;width:621px;height:28px;background:linear-gradient(#f7f7f7,#e8e8e8);border:1px solid var(--card-edge);font-size:12px;font-weight:700;padding:6px 17px}
.card{position:absolute;left:280px;width:621px;height:180px;background:var(--card);border-radius:4px;box-shadow:0 1px 3px rgba(0,0,0,.15)}
.card::before{content:"";position:absolute;left:-9px;top:20px;border:9px solid transparent;border-left-width:0;border-right-color:var(--card)}
.card-photo{position:absolute;left:19px;top:15px;width:106px;height:106px;border-radius:4px;background:linear-gradient(135deg,#8fc6d8,#d9a07e 45%,#1f3552)}
.card-body{position:absolute;left:153px;top:12px;width:450px}
.card-body h3{font-size:19px;font-weight:300;line-height:29px;color:#222}
.pill{display:inline-block;width:56px;height:20px;margin-left:10px;border-radius:3px;background:var(--pill);color:#fff;font-size:11px;font-weight:400;text-align:center;line-height:20px;vertical-align:2px}
.card-body p{font-size:11px;line-height:22px;color:var(--ink-soft);margin-top:7px}
.meta{position:absolute;left:158px;top:146px;width:440px;display:flex;align-items:center;font-size:10px;font-style:italic;color:var(--ink-mute)}
.meta-cell{display:flex;align-items:center;gap:8px;padding-right:20px;margin-right:20px;border-right:1px solid #e2e2e2;height:20px}
.meta-cell:nth-child(3){border:none}
.meta svg{width:14px;height:14px;fill:#999}
.share{margin-left:auto;display:flex;gap:6px}
.share span{width:22px;height:22px;border-radius:50%;background:#e1e3d8;border:2px solid #bfc3b3}

/* leader board */
.board{position:absolute;left:946px;top:125px;width:237px;background:#fff;border:1px solid #ddd;border-collapse:collapse;box-shadow:0 1px 3px rgba(0,0,0,.1)}
.board th{height:34px;background:linear-gradient(#fafafa,#eee);font-size:12px;font-weight:600;text-align:left;padding-left:14px}
.board td{height:45.5px;font-size:10px;font-weight:700;padding-left:14px}
.board td:first-child{font-size:11px;font-weight:400;color:var(--ink-mute)}
.board tr:nth-child(even) td{background:var(--row-alt)}
</style>
</head>
<body>

<header class="topbar">
  <div class="nav-item nav-home">
    <svg viewBox="0 0 16 16"><path d="M1 12a7 7 0 0 1 14 0z" fill="#fff"/></svg>Home<span class="badge">3</span>
  </div>
  <div class="nav-item" style="left:161px"><svg viewBox="0 0 16 16" fill="#fff"><rect x="1" y="2" width="14" height="13" fill="none" stroke="#fff" stroke-width="1.5"/><path d="M4 6h2v2H4zM7 6h2v2H7zM10 6h2v2h-2zM4 10h2v2H4zM7 10h2v2H7zM10 10h2v2h-2z"/></svg>Menu</div>
  <span class="nav-sep" style="left:249px"></span>
  <div class="nav-item" style="left:276px"><svg viewBox="0 0 16 16"><path d="M2 3h7M2 3v11h11V8" fill="none" stroke="#fff" stroke-width="1.8"/><path d="M7 9l7-7" stroke="#fff" stroke-width="1.8"/></svg>Hcp 360</div>
  <span class="nav-sep" style="left:370px"></span>
  <div class="nav-item" style="left:387px"><svg viewBox="0 0 16 16" stroke="#fff" stroke-width="1.6"><path d="M3 1v14M8 1v14M13 1v14"/><path d="M1 5h4M6 11h4M11 6h4"/></svg>Game</div>
  <span class="nav-sep" style="left:479px"></span>
  <div class="top-search"><svg width="15" height="15" viewBox="0 0 16 16"><circle cx="6.5" cy="6.5" r="5" fill="none" stroke="#888" stroke-width="2"/><path d="M10 10l5 5" stroke="#888" stroke-width="2"/></svg>Search...</div>
  <div class="user">
    <svg width="28" height="22" viewBox="0 0 28 22" fill="#fff"><path d="M2 20h24v2H2zM4 8h3v11H4zM9 4h3v15H9zM14 2h3v17h-3zM19 6h3v13h-3z"/></svg>
    <div>Harlan<br>Vey</div>
    <div class="avatar" role="img" aria-label="User profile photo"></div>
  </div>
</header>

<aside class="sidebar">
  <div class="side-title">INDUSTRY NEWS</div>
  <div class="side-search"><svg width="15" height="15" viewBox="0 0 16 16"><circle cx="6.5" cy="6.5" r="5" fill="none" stroke="#333" stroke-width="2"/><path d="M10 10l5 5" stroke="#333" stroke-width="2"/></svg>Search...</div>
  <ul class="side-menu">
    <li><svg viewBox="0 0 28 28"><circle cx="14" cy="8" r="6"/><path d="M3 28q0-12 11-12t11 12z"/></svg>Compliance News</li>
    <li><svg viewBox="0 0 28 28"><ellipse cx="11" cy="12" rx="10" ry="7"/><ellipse cx="19" cy="16" rx="8" ry="6" fill="#d3d6d9"/></svg>Docementry</li>
    <li><svg viewBox="0 0 28 28"><circle cx="10" cy="12" r="5"/><path d="M1 28q0-10 9-10t9 10z"/><ellipse cx="21" cy="6" rx="6" ry="4"/></svg>Compliance Blog</li>
    <li><svg viewBox="0 0 28 28"><circle cx="6" cy="22" r="4"/><rect x="12" y="6" width="12" height="3"/><rect x="12" y="11" width="12" height="3"/><rect x="12" y="16" width="12" height="3"/><rect x="12" y="21" width="12" height="3"/></svg>Relevant Links</li>
    <li><svg viewBox="0 0 28 28"><path d="M2 2v24h24" fill="none" stroke="#b9bcbf" stroke-width="2"/><path d="M5 20l6-7 5 4 9-9" fill="none" stroke="#b9bcbf" stroke-width="2.5"/></svg>Graphics</li>
    <li><svg viewBox="0 0 28 28"><path d="M14 2L1 14h4v12h18V14h4z"/></svg>Home</li>
    <li><svg viewBox="0 0 28 28"><path d="M14 2q8 0 8 10v8l3 4H3l3-4v-8q0-10 8-10z"/></svg>Reports</li>
    <li><svg viewBox="0 0 28 28"><circle cx="14" cy="14" r="12"/></svg>Media Value</li>
  </ul>
  <div class="signin">
    <h2>Sign In</h2>
    <p>Just select your favorite social</p>
    <div class="register">Register here</div>
    <div class="social">
      <span style="background:var(--soc-a)"></span>
      <span style="background:var(--soc-b)"></span>
      <span style="background:var(--soc-c)"></span>
      <span style="background:var(--soc-d)"></span>
    </div>
    <div class="copy">© 2013 All Rights Reserved.</div>
  </div>
</aside>

<main>
  <div class="section-title" style="left:281px;top:95px"><span class="dots"></span>Compliance Game</div>
  <div class="category">CATEGORY ANTI CRUST</div>

  <article class="card" style="top:149px;height:178px">
    <div class="card-photo" role="img" aria-label="Photo of two smiling people"></div>
    <div class="card-body"><h3>Vestibulum nec diam massa, eu ullamcorper mi. Fusce ac erat velit, id lacinia.<span class="pill">ALL</span></h3>
      <p>Plusieurs variations de Lorem Ipsum peuvent être trouvées ici ou là, mais la majeure partie d'entre elles a été altérée par l'addition d'humour ou de mots aléatoires qui ne ressemblent pas.</p></div>
    <div class="meta">
      <div class="meta-cell"><svg viewBox="0 0 16 16"><path d="M1 3h14v12H1zM3 6v7h10V6z"/></svg>March 21st , 2013</div>
      <div class="meta-cell"><svg viewBox="0 0 16 16"><path d="M0 8q8-9 16 0-8 9-16 0z"/><circle cx="8" cy="8" r="2.5" fill="#fff"/></svg>2511</div>
      <div class="meta-cell"><svg viewBox="0 0 16 16"><rect x="1" y="8" width="10" height="7"/><path d="M9 8V5a3 3 0 0 1 6 0" fill="none" stroke="#999" stroke-width="2"/></svg>Public</div>
      <div class="share"><span></span><span></span><span></span></div>
    </div>
  </article>

  <article class="card" style="top:380px">
    <div class="card-photo" role="img" aria-label="Photo of two smiling people"></div>
    <div class="card-body"><h3>Vestibulum nec diam massa, eu ullamcorper mi. Fusce ac erat velit, id lacinia.<span class="pill">ALL</span></h3>
      <p>Plusieurs variations de Lorem Ipsum peuvent être trouvées ici ou là, mais la majeure partie d'entre elles a été altérée par l'addition d'humour ou de mots aléatoires qui ne ressemblent pas.</p></div>
    <div class="meta">
      <div class="meta-cell"><svg viewBox="0 0 16 16"><path d="M1 3h14v12H1zM3 6v7h10V6z"/></svg>March 21st , 2013</div>
      <div class="meta-cell"><svg viewBox="0 0 16 16"><path d="M0 8q8-9 16 0-8 9-16 0z"/><circle cx="8" cy="8" r="2.5" fill="#fff"/></svg>2511</div>
      <div class="meta-cell"><svg viewBox="0 0 16 16"><rect x="1" y="8" width="10" height="7"/><path d="M9 8V5a3 3 0 0 1 6 0" fill="none" stroke="#999" stroke-width="2"/></svg>Public</div>
      <div class="share"><span></span><span></span><span></span></div>
    </div>
  </article>

  <article class="card" style="top:613px">
    <div class="card-photo" role="img" aria-label="Photo of two smiling people"></div>
    <div class="card-body"><h3>Vestibulum nec diam massa, eu ullamcorper mi. Fusce ac erat velit, id lacinia.<span class="pill">ALL</span></h3>
      <p>Plusieurs variations de Lorem Ipsum peuvent être trouvées ici ou là, mais la majeure partie d'entre elles a été altérée par l'addition d'humour ou de mots aléatoires qui ne ressemblent pas.</p></div>
    <div class="meta">
      <div class="meta-cell"><svg viewBox="0 0 16 16"><path d="M1 3h14v12H1zM3 6v7h10V6z"/></svg>March 21st , 2013</div>
      <div class="meta-cell"><svg viewBox="0 0 16 16"><path d="M0 8q8-9 16 0-8 9-16 0z"/><circle cx="8" cy="8" r="2.5" fill="#fff"/></svg>2511</div>
      <div class="meta-cell"><svg viewBox="0 0 16 16"><rect x="1" y="8" width="10" height="7"/><path d="M9 8V5a3 3 0 0 1 6 0" fill="none" stroke="#999" stroke-width="2"/></svg>Public</div>
      <div class="share"><span></span><span></span><span></span></div>
    </div>
  </article>

  <div class="section-title" style="left:946px;top:98px"><span class="dots"></span>Leader Board</div>
  <table class="board">
    <thead><tr><th>Board</th><th>Price</th><th>Date</th></tr></thead>
    <tbody>
      <tr><td>New Events</td><td>$320</td><td>23 Jul 2013</td></tr>
      <tr><td>Archive</td><td>$115</td><td>10 Aug 2013</td></tr>
      <tr><td>Notes Stories</td><td>$45</td><td>15 Sep 2013</td></tr>
      <tr><td>Database</td><td>$4,200</td><td>30 Oct 2013</td></tr>
      <tr><td>Schedule</td><td>$1,050</td><td>1 Nov 2013</td></tr>
      <tr><td>New Events</td><td>$320</td><td>23 Jul 2013</td></tr>
      <tr><td>Archive</td><td>$115</td><td>10 Aug 2013</td></tr>
      <tr><td>Notes Stories</td><td>$45</td><td>15 Sep 2013</td></tr>
      <tr><td>Database</td><td>$4,200</td><td>30 Oct 2013</td></tr>
      <tr><td>Schedule</td><td>$1,050</td><td>1 Nov 2013</td></tr>
      <tr><td>New Events</td><td>$320</td><td>23 Jul 2013</td></tr>
      <tr><td>Archive</td><td>$115</td><td>10 Aug 2013</td></tr>
      <tr><td>Notes Stories</td><td>$45</td><td>15 Sep 2013</td></tr>
      <tr><td>Archive</td><td>$115</td><td>10 Aug 2013</td></tr>
    </tbody>
  </table>
</main>

</body>
</html>
```